Catalogue design for Aluminium Panel and spray painting manufacturer based in Huizhou, China.

Metrovex is a trading company that represent Dansheng metal spraying industry that manufactures aluminium panels and extrusions of all kinds and PVDF coating.

We are a manufacturer and producer of aluminium panels and PVDF painting based in Huizhou, China. We produce aluminium panels that are use widely in subways, shopping malls and construction works both for interior and exterior usage.

Dan Sheng mainly deal with contractors and project managers business within Mainland China and Hong Kong with a select few clientele in Australia and Philippines. We are now looking to expand the business and reach further international businesses.

We therefore need a new brochure to introduce the new trading name Metrovex to further the sales strategy into international borders. As manufacturers are heavily based on credentials and certifications these must be displayed accordingly to gain trust within the construction market.

The following content will be required

1. Who we are and what we do, manufacturer of aluminium panels and PVDF coating.
2. a)Guide to our manufacturing process, bending, cutting, welding of aluminum panels
b)Guide to choice of painting powder coating or PVDF coating. (PVDF being the main choice)
3. a)Some technical information about the core product of aluminium of aluminum panels such as size dimensions, width of panels and grade of aluminium.
b)Information on PVDF painting and a colour chart of either RAL or PANTONE.
4. Projects undertaken and some photos, preferably in a grid 2 column layout as exampled on attached photo.
5. Certifications of factory and office address and contact info.

We are looking for design that can showcase our manufacturing process in a catalogue displaying a consistent colour design theme throughout.

A simple guide of the manufacturing process and including some technical specification about the aluminium panels such as width and maximum dimenstions etc.

Target Market(s)

Asean and south east asia.

Industry/Entity Type

Manufacturer

Contact Information for Business Card

To be in colour theme with the catalogue design. Contain logo and to draw more focus more on the web url.

Colors
ec1f27

Requirements
Must have
• Must include a colour theme that is striking throughout the catalogue and easy to look at graphical layout. A graphical view without too much text aside from the technical specifications.
• Certifications of manufacturer. ISO, Verlo Danth etc( as displayed within company profile PDF)
Nice to have
• A consistent usage of photos without too obvious generic building photos.
• A well displayed layout for each page.
• Perhaps a three toned colour theme that works according with the logo. Perhaps some red throughout on a black main colour. Contrasting colours without an overwash of one colour.
Should not have
• Generic photos of office people or overly enthusiastic business people.
• With Exception of photos shots of the factory workers.

```html
<!DOCTYPE html>
<html lang="en">
<head>
<meta charset="utf-8">
<title>Metrovex Catalogue Covers</title>
<link rel="stylesheet" href="https://fonts.googleapis.com/css2?family=Roboto:wght@400;500&family=Oswald:wght@500&display=swap">
<style>
  :root {
    --canvas: #e9e4dc;
    --cream: #f7eadd;
    --cream-deep: #efdccb;
    --wine: #7b1419;
    --red: #c8202a;
    --red-bright: #ec1f27;
    --ink-red: #8e1a20;
  }
  * { margin: 0; padding: 0; box-sizing: border-box; }
  html, body { width: 1200px; height: 1200px; overflow: hidden; }
  body { background: var(--canvas); font-family: "Roboto", sans-serif; position: relative; }

  .cover {
    position: absolute; left: 100px; width: 1000px; height: 480px;
    background: var(--cream); overflow: hidden;
    box-shadow: 0 6px 18px rgba(0,0,0,.18);
  }
  .cover--front { top: 90px; }
  .cover--back { top: 630px; }
  .cover-art { position: absolute; inset: 0; width: 100%; height: 100%; }

  .brand { position: absolute; display: flex; align-items: center; gap: 12px; }
  .brand-square { background: var(--wine); border-radius: 8px; }
  .brand-name { font-family: "Roboto", sans-serif; font-weight: 500; color: var(--wine); letter-spacing: .5px; }
  .cover--front .brand { left: 100px; top: 36px; }
  .cover--front .brand-square { width: 48px; height: 48px; }
  .cover--front .brand-name { font-size: 40px; }
  .cover--back .brand { left: 80px; top: 58px; gap: 8px; }
  .cover--back .brand-square { width: 26px; height: 26px; border-radius: 5px; }
  .cover--back .brand-name { font-size: 21px; }

  .photo { position: absolute; }
  .photo--lobby {
    left: 100px; top: 112px; width: 880px; height: 326px;
    background: linear-gradient(115deg, #8a7a3e 0%, #b7a45e 35%, #c9b98a 55%, #8d6f45 80%, #5a4a30 100%);
  }
  .photo--living {
    left: 270px; top: 128px; width: 440px; height: 236px;
    border: 6px solid var(--red);
    background: linear-gradient(120deg, #e9e2d4 0%, #b79a86 35%, #8c4a2e 65%, #b36a3a 100%);
  }

  .contact { position: absolute; left: 448px; top: 370px; color: var(--ink-red); }
  .contact-title { font-family: "Oswald", sans-serif; font-weight: 500; font-size: 20px; letter-spacing: .5px; line-height: 1.1; margin-bottom: 3px; }
  .contact-list { list-style: none; font-size: 12px; line-height: 15px; }
  .contact-list li { display: flex; align-items: center; gap: 6px; }
  .contact-list svg { width: 10px; height: 10px; fill: var(--ink-red); }
</style>
</head>
<body>

<section class="cover cover--front">
  <svg class="cover-art" viewBox="0 0 1000 480" aria-hidden="true">
    <rect class="spine" x="0" y="0" width="60" height="480" fill="var(--wine)"/>
    <rect x="70" y="0" width="3" height="480" fill="var(--red)"/>
    <g class="corner-lines" stroke="var(--red)" stroke-width="3" fill="none">
      <polyline points="320,14 972,14 972,96"/>
      <polyline points="420,26 958,26 958,88"/>
      <polyline points="520,38 944,38 944,80"/>
    </g>
    <rect x="100" y="102" width="880" height="4" fill="var(--red)"/>
    <rect x="190" y="452" width="810" height="10" fill="var(--red)"/>
  </svg>
  <div class="brand">
    <span class="brand-square"></span>
    <span class="brand-name">Metrovex</span>
  </div>
  <div class="photo photo--lobby" role="img" aria-label="Photo of a bright lobby interior with arched doorway, round mirror, armchairs and tall windows"></div>
  <svg class="cover-art" viewBox="0 0 1000 480" aria-hidden="true">
    <g class="facets">
      <polygon points="760,112 850,112 800,175" fill="var(--red)"/>
      <polygon points="800,175 850,112 900,180" fill="var(--wine)"/>
      <polygon points="900,112 980,112 940,170" fill="var(--red)"/>
      <polygon points="800,175 900,180 850,250" fill="var(--red-bright)"/>
      <polygon points="850,250 900,180 960,260" fill="var(--wine)"/>
      <polygon points="900,180 980,170 960,260" fill="var(--red)"/>
      <polygon points="880,290 980,270 940,340" fill="var(--red)"/>
    </g>
  </svg>
</section>

<section class="cover cover--back">
  <svg class="cover-art" viewBox="0 0 1000 480" aria-hidden="true">
    <rect class="spine" x="940" y="0" width="60" height="480" fill="var(--wine)"/>
    <rect x="925" y="0" width="3" height="480" fill="var(--red)"/>
    <g class="corner-lines" stroke="var(--red)" stroke-width="3" fill="none">
      <polyline points="18,110 18,18 520,18"/>
      <polyline points="30,100 30,30 440,30"/>
      <polyline points="42,90 42,42 360,42"/>
    </g>
    <rect x="60" y="292" width="865" height="3" fill="var(--red)"/>
    <rect x="150" y="462" width="775" height="9" fill="var(--red)"/>
    <g class="facets">
      <polygon points="620,20 660,70 580,70" fill="var(--wine)"/>
      <polygon points="520,70 550,100 490,100" fill="var(--red)"/>
      <polygon points="560,90 600,90 585,120" fill="var(--wine)"/>
      <polygon points="520,110 550,135 495,135" fill="var(--wine)"/>
      <polygon points="410,80 450,128 370,128" fill="var(--wine)"/>
      <polygon points="430,100 490,100 455,140" fill="var(--red)"/>
      <polygon points="330,90 370,128 290,128" fill="var(--red-bright)"/>
      <polygon points="360,100 410,80 395,128" fill="var(--red)"/>
    </g>
  </svg>
  <div class="brand">
    <span class="brand-square"></span>
    <span class="brand-name">Metrovex</span>
  </div>
  <div class="photo photo--living" role="img" aria-label="Photo of a living room with fireplace, bookshelves, floral sofa and wooden floor"></div>
  <div class="contact">
    <h2 class="contact-title">CONTACT INFO</h2>
    <ul class="contact-list">
      <li><svg viewBox="0 0 10 10"><path d="M5 0a3.5 3.5 0 0 0-3.5 3.5C1.5 6 5 10 5 10s3.5-4 3.5-6.5A3.5 3.5 0 0 0 5 0zm0 5a1.5 1.5 0 1 1 0-3 1.5 1.5 0 0 1 0 3z"/></svg>150 Lorem Ipsum, Lorem Ipsum</li>
      <li><svg viewBox="0 0 10 10"><path d="M2 0l2 2.5-1 1.2a6 6 0 0 0 3.3 3.3l1.2-1L10 8l-1.5 2C4 10 0 6 0 1.5z"/></svg>123.456.7890</li>
      <li><svg viewBox="0 0 10 10"><path d="M0 2h10v6H0zM0 2l5 3.5L10 2" /></svg>info@metrovex.com</li>
      <li><svg viewBox="0 0 10 10"><circle cx="5" cy="5" r="4.5"/></svg>www.metrovex.com</li>
    </ul>
  </div>
</section>

</body>
</html>
```